TG - management consultant

Business card - contemporary design

Front info
Thomas Galloway

(Address not necessary)
PO Box 7324
Belmont, CA 94002

(650) 482-3719
tg@thomasgallo.wy

Twitter: tgq287
Facebook: /Thomas.Galloway
Linkedin: /in/thomasgalloway

Back or Front
www.thomasgalloway.net
Facilitation & coaching, change management, strategic partnerships, business improvement

Target Market(s)

High tech businesses - mostly startups in Silicon Valley

Industry/Entity Type

Business

Font styles to use
Sans Serif

Colors

Designer to choose colors to be used in the design.

```html
<!DOCTYPE html>
<html lang="en">
<head>
<meta charset="utf-8">
<title>Thomas Galloway – Business Card</title>
<link rel="stylesheet" href="https://fonts.googleapis.com/css2?family=Open+Sans:wght@400;600;700&family=Quicksand:wght@400;500&display=swap">
<style>
  :root {
    --canvas-bg: #e4e4e2;
    --card-white: #f1f1ef;
    --card-dark-start: #50555b;
    --card-dark-end: #1c1f23;
    --band-dark: #1f2226;
    --ink-grey: #5c5f63;
    --ink-light: #e6e7e8;
    --accent-orange: #e5962b;
  }
  * { margin: 0; padding: 0; box-sizing: border-box; }
  html, body {
    width: 1200px;
    height: 873px;
    overflow: hidden;
    background: var(--canvas-bg);
  }
  .canvas {
    position: relative;
    width: 1200px;
    height: 873px;
  }
  .card {
    position: absolute;
    top: 286px;
    width: 540px;
    height: 300px;
    box-shadow: 0 6px 18px rgba(0,0,0,0.18);
    overflow: hidden;
  }
  .card--back {
    left: 40px;
    background: linear-gradient(90deg, var(--card-dark-start) 0%, #2b2f34 55%, var(--card-dark-end) 100%);
    font-family: "Quicksand", sans-serif;
    color: var(--ink-light);
    text-align: center;
  }
  .services {
    position: absolute;
    top: 112px;
    left: 0;
    right: 0;
    font-size: 18px;
    line-height: 26px;
    font-weight: 400;
  }
  .back-url {
    position: absolute;
    top: 170px;
    left: 0;
    right: 0;
    font-size: 16px;
    color: var(--accent-orange);
  }
  .card--front {
    left: 620px;
    background: var(--card-white);
    font-family: "Open Sans", sans-serif;
  }
  .front-band {
    position: absolute;
    left: 0;
    right: 0;
    bottom: 0;
    height: 12px;
    background: var(--band-dark);
  }
  .identity {
    position: absolute;
    right: 24px;
    top: 82px;
    text-align: right;
  }
  .identity__name {
    font-size: 22px;
    font-weight: 700;
    color: var(--ink-grey);
    line-height: 26px;
  }
  .identity__title {
    font-size: 16px;
    color: var(--accent-orange);
    line-height: 20px;
  }
  .contacts {
    position: absolute;
    right: 24px;
    top: 150px;
    list-style: none;
  }
  .contact {
    display: flex;
    justify-content: flex-end;
    align-items: center;
    gap: 8px;
    font-size: 17px;
    line-height: 20px;
    color: var(--ink-grey);
  }
  .contact--web { color: var(--accent-orange); }
  .contact svg { width: 15px; height: 15px; flex: none; }
</style>
</head>
<body>
<main class="canvas">
  <section class="card card--back" aria-label="Card back">
    <p class="services">Facilitation &amp; coaching | change management,<br>strategic partnerships | business improvement</p>
    <p class="back-url">www.thomasgalloway.net</p>
  </section>

  <section class="card card--front" aria-label="Card front">
    <div class="identity">
      <h1 class="identity__name">Thomas Galloway</h1>
      <p class="identity__title">Executive Advisor</p>
    </div>
    <ul class="contacts">
      <li class="contact">(650) 482-3719
        <svg viewBox="0 0 15 15" aria-hidden="true"><rect x="4" y="1" width="7" height="13" rx="1.5" fill="none" stroke="#e5962b" stroke-width="1.5"/><line x1="6.5" y1="12" x2="8.5" y2="12" stroke="#e5962b" stroke-width="1"/></svg>
      </li>
      <li class="contact">tg@thomasgallo.wy
        <svg viewBox="0 0 15 15" aria-hidden="true"><rect x="1" y="3" width="13" height="9" fill="#e5962b"/><polyline points="1.5,3.5 7.5,8.5 13.5,3.5" fill="none" stroke="#f1f1ef" stroke-width="1.2"/></svg>
      </li>
      <li class="contact">/in/thomasgalloway
        <svg viewBox="0 0 15 15" aria-hidden="true"><rect x="1.5" y="1.5" width="12" height="12" fill="#e5962b"/></svg>
      </li>
      <li class="contact contact--web">www.thomasgalloway.net
        <svg viewBox="0 0 15 15" aria-hidden="true"><rect x="1" y="2" width="13" height="9" fill="none" stroke="#e5962b" stroke-width="1.5"/><line x1="5" y1="13.5" x2="10" y2="13.5" stroke="#e5962b" stroke-width="1.5"/></svg>
      </li>
    </ul>
    <div class="front-band"></div>
  </section>
</main>
</body>
</html>
```